eCommerce Website Design for Children's Book Service

I am looking for a 5 page eCommerce website that includes a Shopping Cart. 'Tullow Books' is the title of the company and its logo is attached. 'Sprouting wonder in words,' is the company's motto and 'spring green' is the main color. The website needs to appeal to families. Images of books and/or maple seeds (helicopter seeds) moving are part of the graphics.
Updates

I have updated my brief and I would like my website design to include 5 pages: home, about, products (books), blog, contact. WordPress is the web format that I am most comfortable with.

Target Market(s)

Families with young children

Coding

Coded - Design and coding required

Number of Pages Required

5+ page

Requirements
Must have
• Shopping cart page; contact page, books page with spaces of photos to go, blog page; spring green color
Nice to have
• A graphic that relates to motto : "sprouting wonder in words"
• WordPress

```html
<!DOCTYPE html>
<html lang="en">
<head>
<meta charset="utf-8">
<title>Tullow Books</title>
<link href="https://fonts.googleapis.com/css2?family=Amaranth:ital,wght@0,400;0,700;1,400;1,700&family=Roboto:wght@400;500&display=swap" rel="stylesheet">
<style>
:root{
  --green:#5eb246;
  --green-dark:#3d9129;
  --green-head:#6cb64c;
  --tint:#f1f8ea;
  --text:#444;
  --muted:#666;
  --card-line:#9fd6cf;
  --star:#e98a2a;
  --white:#fff;
}
*{margin:0;padding:0;box-sizing:border-box}
html,body{width:1200px;height:2995px;overflow:hidden}
body{position:relative;background:var(--white);font-family:Roboto,Arial,sans-serif;color:var(--text)}
.abs{position:absolute}
.display{font-family:Amaranth,sans-serif;font-style:italic}

.topline{left:0;top:0;width:1200px;height:4px;background:var(--green)}
.hero{left:0;top:4px;width:1200px;height:676px;background:linear-gradient(120deg,#4a3b2c 0%,#8a7456 35%,#c4a86a 55%,#7d6a4a 75%,#3b3226 100%)}
.hero-wave{left:0;top:660px;width:1200px;height:40px}
.brand{left:110px;top:110px;font-family:Amaranth,sans-serif;font-weight:700;font-size:40px;color:var(--green);display:flex;align-items:center;gap:10px}
.brand .dot{width:18px;height:18px;border-radius:50%;background:var(--green)}
.nav{top:48px;left:436px;display:flex;gap:0;font-size:13px;font-weight:500;color:#333}
.nav a{text-decoration:none;color:#333;display:block;padding:0 20px}
.nav a.active{color:var(--green)}
.hero-title{left:112px;top:310px;color:var(--white);font-family:Amaranth,sans-serif;line-height:1}
.hero-title .small{font-size:50px;display:block}
.hero-title .big{font-size:72px;display:block;margin-top:6px}
.btn{background:var(--green);color:var(--white);border-radius:24px;font-family:Amaranth,sans-serif;font-size:19px;display:flex;align-items:center;justify-content:center}
.shop{left:112px;top:466px;width:132px;height:46px}
.arrow{width:34px;height:34px;border-radius:50%;border:2px solid var(--white);top:391px;display:flex;align-items:center;justify-content:center}

.promo{top:726px;width:316px;height:230px;background:var(--green);padding:10px}
.promo .inner{width:100%;height:100%;border:2px solid rgba(255,255,255,.8);position:relative;color:var(--white)}
.promo.mid{background:var(--green-dark)}
.promo .art{position:absolute;background:linear-gradient(160deg,#f2c79a,#d9534f 60%,#3a7bd5);border-radius:6px}
.promo h3{font-family:Amaranth,sans-serif;font-weight:400;position:absolute}
.promo p{font-family:Amaranth,sans-serif;font-style:italic;font-size:15px;position:absolute}

.tint{left:0;top:996px;width:1200px;height:630px;background:var(--tint)}
.sec-title{width:1200px;left:0;text-align:center;font-family:Amaranth,sans-serif;font-style:italic;font-size:40px;color:var(--green-head)}
.sec-sub{width:1200px;left:0;text-align:center;font-size:12px;color:var(--muted)}

.card{width:226px;height:360px;border:1.5px dashed var(--card-line);background:var(--white);text-align:center}
.card .cover{position:absolute;left:52px;top:34px;width:124px;height:200px;border-radius:3px}
.card .tag{position:absolute;left:8px;top:12px;font-family:Amaranth,sans-serif;font-size:15px;color:var(--white);padding:2px 10px}
.card .stars{position:absolute;left:0;width:100%;top:246px;color:var(--star);font-size:15px;letter-spacing:2px}
.card .name{position:absolute;left:0;width:100%;top:270px;font-family:Amaranth,sans-serif;font-size:22px;color:#333}
.card .price{position:absolute;left:0;width:100%;top:306px;font-size:22px;color:var(--green)}

.offers{left:0;top:1626px;width:1200px;height:334px;background:linear-gradient(180deg,#63b54b,#4ea534)}
.offer-book{left:150px;top:1575px;width:258px;height:450px;background:linear-gradient(180deg,#cfe9d9 0%,#8cc8a0 45%,#c34a62 75%,#7a4d8a 100%);border-radius:4px}
.offer-kid{left:880px;top:1690px;width:280px;height:275px;background:radial-gradient(circle at 60% 45%,#f3c9a8 0%,#e07b52 35%,#9fdcc6 65%,rgba(159,220,198,0) 80%)}
.offers-title{left:456px;top:1684px;font-family:Amaranth,sans-serif;font-size:60px;color:var(--white)}
.offers-text{left:458px;top:1772px;width:440px;font-family:Amaranth,sans-serif;font-style:italic;font-size:17px;line-height:26px;color:#e8f6df}
.offers-deal{left:456px;top:1850px;font-family:Amaranth,sans-serif;font-size:32px;color:var(--white)}

.footer{left:0;top:2556px;width:1200px;height:439px;background:var(--green);color:var(--white)}
.feature-icon{width:84px;height:84px;border-radius:50%;background:var(--white);display:flex;align-items:center;justify-content:center}
.feature h4{font-family:Amaranth,sans-serif;font-style:italic;font-weight:400;font-size:18px}
.feature p{font-size:12px;line-height:20px;margin-top:6px;width:200px;color:#eaf6e3}
.dash-h{height:0;border-top:1.5px dashed rgba(255,255,255,.6)}
.dash-v{width:0;border-left:1.5px dashed rgba(255,255,255,.6)}
.col{text-align:center}
.col h4{font-family:Amaranth,sans-serif;font-weight:400;font-size:30px}
.col p{font-size:12px;line-height:20px;color:#eaf6e3}
.phone-num{font-family:Amaranth,sans-serif;font-size:34px}
.email-box{left:470px;top:2850px;width:272px;height:42px;background:var(--white);border-radius:21px;font-family:Amaranth,sans-serif;font-style:italic;font-size:13px;color:#333;padding:13px 24px}
.subscribe{left:474px;top:2906px;width:134px;height:40px;background:var(--green-dark);font-size:18px}
.copy{left:800px;top:2955px;font-size:12px;color:#eaf6e3}
</style>
</head>
<body>
<div class="abs hero" role="img" aria-label="Photo of a young girl reading a book beside stacks of books"></div>
<div class="abs topline"></div>
<svg class="abs hero-wave" viewBox="0 0 1200 40" preserveAspectRatio="none"><path d="M0 20 Q15 8 30 20 T60 20 T90 20 T120 20 T150 20 T180 20 T210 20 T240 20 T270 20 T300 20 T330 20 T360 20 T390 20 T420 20 T450 20 T480 20 T510 20 T540 20 T570 20 T600 20 T630 20 T660 20 T690 20 T720 20 T750 20 T780 20 T810 20 T840 20 T870 20 T900 20 T930 20 T960 20 T990 20 T1020 20 T1050 20 T1080 20 T1110 20 T1140 20 T1170 20 T1200 20 V40 H0Z" fill="#fff"/></svg>

<div class="abs brand"><span class="dot"></span>Tullow Books</div>
<nav class="abs nav"><a class="active" href="#">HOME</a><a href="#">ABOUT US</a><a href="#">SERVICES</a><a href="#">PRODUCTS</a><a href="#">NEWS</a><a href="#">CONTACT US</a></nav>
<h1 class="abs hero-title"><span class="small">Sprouting</span><span class="big">wonder in words</span></h1>
<div class="abs btn shop">Shop Now</div>
<div class="abs arrow" style="left:67px"><svg width="12" height="12" viewBox="0 0 12 12"><path d="M8 1 L3 6 L8 11" stroke="#fff" stroke-width="2" fill="none"/></svg></div>
<div class="abs arrow" style="left:1099px"><svg width="12" height="12" viewBox="0 0 12 12"><path d="M4 1 L9 6 L4 11" stroke="#fff" stroke-width="2" fill="none"/></svg></div>

<div class="abs promo" style="left:112px"><div class="inner">
  <div class="art" role="img" aria-label="Illustration of two children reading on a pile of books" style="left:-2px;top:20px;width:140px;height:175px"></div>
  <h3 style="left:136px;top:24px;font-size:44px">Big Sale</h3>
  <p style="left:138px;top:90px">Sed ut perspiciatis unde</p>
</div></div>
<div class="abs promo mid" style="left:442px"><div class="inner" style="text-align:center">
  <h3 style="left:0;width:100%;top:24px;font-size:34px">Gift Voucher</h3>
  <p style="left:0;width:100%;top:82px;font-size:13px;font-style:normal">Thank you for shopping with us!</p>
  <p style="left:0;width:100%;top:108px;font-size:13px;font-style:normal">Save 50% off if you enter promo code</p>
  <div class="abs" style="left:88px;top:154px;width:136px;height:36px;border:1.5px solid #fff;border-radius:18px;font-family:Amaranth,sans-serif;font-size:14px;line-height:33px">View More</div>
</div></div>
<div class="abs promo" style="left:774px;background:#7fc464"><div class="inner">
  <div class="art" role="img" aria-label="Photo of a girl sitting and reading a red book" style="left:-2px;top:10px;width:140px;height:190px;background:linear-gradient(180deg,#f0d2b8,#e5534b 50%,#f2f2f2)"></div>
  <h3 style="left:136px;top:40px;font-size:44px">Special</h3>
  <p style="left:138px;top:106px">Sed ut perspiciatis unde</p>
</div></div>

<div class="abs tint"></div>
<h2 class="abs sec-title" style="top:1022px">New Arrivals</h2>
<p class="abs sec-sub" style="top:1088px">Sed ut perspiciatis unde omnis iste natus error sit voluptatem accusantium doloremque laudantium</p>

<div class="abs card" style="left:112px;top:1156px"><div class="cover" role="img" aria-label="Pink children's book cover" style="background:linear-gradient(135deg,#e9469a,#f37cb5)"></div><span class="tag" style="background:#ec5fa3">Sale</span><div class="stars">☆☆☆☆☆</div><div class="name">Product Name</div><div class="price">$ 250.00</div></div>
<div class="abs card" style="left:362px;top:1156px"><div class="cover" role="img" aria-label="Teal children's book cover" style="background:linear-gradient(135deg,#1aa6c8,#3cc3de)"></div><div class="stars">☆☆☆☆☆</div><div class="name">Product Name</div><div class="price">$ 250.00</div></div>
<div class="abs card" style="left:612px;top:1156px"><div class="cover" role="img" aria-label="Yellow children's book cover" style="background:linear-gradient(135deg,#f2c010,#f7d94a)"></div><span class="tag" style="background:#f2c010">Sale</span><div class="stars">☆☆☆☆☆</div><div class="name">Product Name</div><div class="price">$ 250.00</div></div>
<div class="abs card" style="left:862px;top:1156px"><div class="cover" role="img" aria-label="Lime green children's book cover" style="background:linear-gradient(135deg,#8dbb12,#b0d53a)"></div><div class="stars">☆☆☆☆☆</div><div class="name">Product Name</div><div class="price">$ 250.00</div></div>

<div class="abs offers"></div>
<div class="abs offer-book" role="img" aria-label="Illustrated book cover with a girl on a stack of books"></div>
<div class="abs offer-kid" role="img" aria-label="Illustration of a girl reading a magical red book"></div>
<h2 class="abs offers-title">Special Offers</h2>
<p class="abs offers-text">Sed ut perspiciatis unde omnis iste natus error sit voluptatem accusantium doloremque laudantium</p>
<div class="abs offers-deal">Upto 50% off</div>

<h2 class="abs sec-title" style="top:2016px">Best Sellers</h2>
<p class="abs sec-sub" style="top:2082px">Sed ut perspiciatis unde omnis iste natus error sit voluptatem accusantium doloremque laudantium</p>

<div class="abs card" style="left:112px;top:2140px"><div class="cover" role="img" aria-label="Purple children's book cover" style="background:linear-gradient(135deg,#7d4ee0,#9c74ef)"></div><span class="tag" style="background:#ec5fa3">Sale</span><div class="stars">☆☆☆☆☆</div><div class="name">Product Name</div><div class="price">$ 250.00</div></div>
<div class="abs card" style="left:362px;top:2140px"><div class="cover" role="img" aria-label="Green children's book cover" style="background:linear-gradient(135deg,#3fbf3a,#6ad35f)"></div><div class="stars">☆☆☆☆☆</div><div class="name">Product Name</div><div class="price">$ 250.00</div></div>
<div class="abs card" style="left:612px;top:2140px"><div class="cover" role="img" aria-label="Orange children's book cover" style="background:linear-gradient(135deg,#f04a1c,#f77a3c)"></div><span class="tag" style="background:#f2c010">Sale</span><div class="stars">☆☆☆☆☆</div><div class="name">Product Name</div><div class="price">$ 250.00</div></div>
<div class="abs card" style="left:862px;top:2140px"><div class="cover" role="img" aria-label="Blue children's book cover" style="background:linear-gradient(135deg,#1279b8,#2aa0d6)"></div><div class="stars">☆☆☆☆☆</div><div class="name">Product Name</div><div class="price">$ 250.00</div></div>

<footer class="abs footer">
  <div class="abs feature" style="left:110px;top:44px;display:flex;gap:14px">
    <div class="feature-icon"><svg width="40" height="28" viewBox="0 0 40 28"><rect x="2" y="4" width="22" height="16" fill="none" stroke="#5eb246" stroke-width="2.5"/><path d="M24 9 H32 L37 15 V20 H24Z" fill="none" stroke="#5eb246" stroke-width="2.5"/><circle cx="10" cy="23" r="3" fill="#5eb246"/><circle cx="30" cy="23" r="3" fill="#5eb246"/></svg></div>
    <div><h4>Free Shipping Item</h4><p>Sed ut perspiciatis unde omnis iste error sit voluptatem</p></div>
  </div>
  <div class="abs feature" style="left:442px;top:44px;display:flex;gap:14px">
    <div class="feature-icon"><svg width="36" height="28" viewBox="0 0 36 28"><rect x="2" y="4" width="32" height="20" rx="3" fill="none" stroke="#5eb246" stroke-width="2.5"/><rect x="2" y="9" width="32" height="4" fill="#5eb246"/></svg></div>
    <div><h4>Secured Payment</h4><p>Sed ut perspiciatis unde omnis iste error sit voluptatem</p></div>
  </div>
  <div class="abs feature" style="left:774px;top:44px;display:flex;gap:14px">
    <div class="feature-icon"><svg width="30" height="36" viewBox="0 0 30 36"><circle cx="15" cy="13" r="10" fill="none" stroke="#5eb246" stroke-width="2.5"/><path d="M9 21 L6 34 L15 29 L24 34 L21 21" fill="none" stroke="#5eb246" stroke-width="2.5"/></svg></div>
    <div><h4>Money Back Guarantee</h4><p>Sed ut perspiciatis unde omnis iste error sit voluptatem</p></div>
  </div>
  <div class="abs dash-h" style="left:110px;top:154px;width:980px"></div>
  <div class="abs dash-v" style="left:428px;top:154px;height:285px"></div>
  <div class="abs dash-v" style="left:772px;top:154px;height:285px"></div>

  <div class="abs col" style="left:110px;top:176px;width:280px">
    <h4>Need Help?</h4>
    <p style="margin-top:8px">Sed ut perspiciatis unde omnis iste natus error sit voluptatem accusantium</p>
    <svg style="margin-top:14px" width="50" height="44" viewBox="0 0 50 44"><path d="M4 14 Q25 0 46 14 L40 18 Q25 10 10 18Z" fill="none" stroke="#fff" stroke-width="2.5"/><rect x="10" y="20" width="30" height="22" rx="3" fill="none" stroke="#fff" stroke-width="2.5"/><path d="M17 27h4M23 27h4M29 27h4M17 33h4M23 33h4M29 33h4" stroke="#fff" stroke-width="2.5"/></svg>
    <div class="phone-num">(000)-555-0142</div>
  </div>
  <div class="abs col" style="left:456px;top:176px;width:300px">
    <h4>Newsletter</h4>
    <p style="margin-top:8px">Sed ut perspiciatis unde omnis iste natus error sit voluptatem accusantium</p>
  </div>
  <div class="abs col" style="left:800px;top:176px;width:300px">
    <h4>Contact Us</h4>
    <svg style="margin-top:6px" width="18" height="16" viewBox="0 0 18 16"><path d="M9 1 L1 8 H3 V15 H7 V10 H11 V15 H15 V8 H17Z" fill="#fff"/></svg>
    <p>Address : # 145 Lorem Ipsum Dummy Text<br>Lorem Ipsum Ipsum Dummy</p>
    <svg style="margin-top:8px" width="20" height="14" viewBox="0 0 20 14"><rect x="1" y="1" width="18" height="12" fill="none" stroke="#fff" stroke-width="1.6"/><path d="M1 1 L10 8 L19 1" fill="none" stroke="#fff" stroke-width="1.6"/></svg>
    <p>hello@tullowbooks.com<br>www.tullowbooks.com</p>
  </div>
</footer>
<div class="abs email-box">Enter Your Email :</div>
<div class="abs btn subscribe">Subscribe</div>
<div class="abs copy">© Copyright 2019 Tullow Books All Rights Reserved</div>
</body>
</html>
```